Business Coach needs an elegant business card design

I need a business card design based around my logo for color and to look like a millionaire dollar coach. Incorporate the color of my logo with something creative and attractive that stands out. I am focused on high end companies and the card must look and feel that way.

Target Market(s)

High End Companies and Business Owners - Training People to become millionaires

Industry/Entity Type

Business

Requirements
Must have
• Front -
Logo (attached file) - Website (kolverbask.com) - Name (Darvel Kemp) Phone (412.807.5531) - Email (darvel@kolverbask.com) (My Title - Success Coach)
Back -
Slogan - Vision (see it) . Action (do it) . Transformation (be it)
Website - Learn More @ kolverbask.com

Creative High End Look!
Nice to have
Should not have
• Cheap standard look
nothing traditional

```html
<!DOCTYPE html>
<html lang="en">
<head>
<meta charset="utf-8">
<title>Darvel Kemp Coaching – Business Cards</title>
<link href="https://fonts.googleapis.com/css2?family=Arimo:wght@400;700&display=swap" rel="stylesheet">
<style>
  :root {
    --stage: #d9d6d2;
    --card-black: #0b0b0b;
    --card-sheen: #3a3a3a;
    --card-mid: #1c1c1c;
    --white: #ffffff;
    --faint-grey: #333333;
    --pattern-tone: rgba(70, 70, 70, .45);
  }
  * { margin: 0; padding: 0; box-sizing: border-box; }
  html, body {
    width: 1200px; height: 855px; overflow: hidden;
    background: var(--stage);
    font-family: "Arimo", Arial, sans-serif;
    color: var(--white);
  }
  .stage { position: relative; width: 1200px; height: 855px; }

  .card {
    position: absolute;
    border: 5px solid var(--white);
    background: linear-gradient(115deg, var(--card-black) 0%, var(--card-mid) 35%, var(--card-sheen) 48%, var(--card-mid) 58%, var(--card-black) 100%);
    box-shadow: 0 12px 30px rgba(0,0,0,.35);
    overflow: hidden;
  }

  /* Back card */
  .card-back { left: 70px; top: 250px; width: 600px; height: 343px; }
  .back-mark {
    position: absolute; left: 0; right: 0; top: 60px;
    display: flex; justify-content: center; align-items: center; gap: 16px;
  }
  .back-mark .ring {
    width: 100px; height: 100px; border-radius: 50%;
    border: 8px solid var(--faint-grey); background: #161616;
  }
  .back-mark .mark-name {
    font-size: 22px; font-weight: 400; color: var(--faint-grey);
    letter-spacing: 2px; text-transform: uppercase;
  }
  .slogan {
    position: absolute; right: 30px; bottom: 92px;
    font-size: 15px; letter-spacing: .3px; white-space: nowrap;
  }
  .learn-row {
    position: absolute; left: 0; right: 0; bottom: 60px;
    display: flex; justify-content: flex-end; align-items: center; gap: 10px;
  }
  .learn-row .bar { height: 6px; width: 12px; background: var(--white); }
  .learn-row .learn-more { font-size: 14px; white-space: nowrap; }
  .back-band {
    position: absolute; left: 0; right: 0; bottom: 22px; height: 14px;
    background: var(--white);
  }

  /* Front card */
  .card-front { left: 770px; top: 100px; width: 360px; height: 630px; }
  .pattern-field {
    position: absolute; left: 0; right: 0; top: 100px; height: 420px;
    background: radial-gradient(ellipse 70% 55% at 50% 50%, var(--pattern-tone) 0%, rgba(40,40,40,.2) 55%, transparent 80%);
  }
  .front-logo {
    position: absolute; left: 24px; top: 36px;
    display: flex; align-items: center; gap: 12px;
  }
  .front-logo .ring {
    width: 58px; height: 58px; border-radius: 50%;
    border: 5px solid var(--white); background: var(--card-black);
  }
  .front-logo .logo-name {
    font-size: 24px; font-weight: 400; letter-spacing: 1.5px;
    text-transform: uppercase; line-height: 1.15;
  }
  .identity {
    position: absolute; right: 26px; top: 450px; text-align: right;
  }
  .identity .name { font-size: 24px; font-weight: 700; letter-spacing: 1px; text-transform: uppercase; }
  .identity .title { font-size: 19px; letter-spacing: 1px; text-transform: uppercase; margin-top: 2px; }
  .contacts {
    position: absolute; right: 26px; top: 530px;
    list-style: none; text-align: right; font-size: 15px; line-height: 22px;
  }
  .contacts li { display: flex; justify-content: flex-end; align-items: center; gap: 8px; }
  .contacts svg { width: 16px; height: 16px; flex: none; }
</style>
</head>
<body>
<main class="stage">

  <section class="card card-back" aria-label="Card back">
    <div class="back-mark">
      <div class="ring"></div>
      <span class="mark-name">Darvel Kemp</span>
    </div>
    <p class="slogan">VISION (SEE IT) . ACTION (DO IT) . TRANSFORMATION (BE IT)</p>
    <div class="learn-row">
      <span class="bar"></span>
      <span class="learn-more">Learn More @ kolverbask.com</span>
      <span class="bar"></span>
    </div>
    <div class="back-band"></div>
  </section>

  <section class="card card-front" aria-label="Card front">
    <div class="pattern-field" role="img" aria-label="Faint tiled monogram pattern in dark grey behind the card content"></div>
    <div class="front-logo">
      <div class="ring"></div>
      <span class="logo-name">Darvel Kemp<br>Coaching</span>
    </div>
    <div class="identity">
      <p class="name">Darvel Kemp</p>
      <p class="title">Success Coach</p>
    </div>
    <ul class="contacts">
      <li>412.807.5531
        <svg viewBox="0 0 16 16" aria-hidden="true"><rect x="1" y="1" width="14" height="14" rx="3" fill="#fff"/><path d="M5 4h2l1 2-1 1c.5 1 1.5 2 2 2l1-1 2 1v2c-4 0-7-3-7-7z" fill="#000"/></svg>
      </li>
      <li>darvel@kolverbask.com
        <svg viewBox="0 0 16 16" aria-hidden="true"><rect x="1" y="1" width="14" height="14" rx="3" fill="#fff"/><rect x="4" y="5" width="8" height="6" fill="none" stroke="#000"/><path d="M4 5l4 3 4-3" fill="none" stroke="#000"/></svg>
      </li>
      <li>kolverbask.com
        <svg viewBox="0 0 16 16" aria-hidden="true"><rect x="1" y="1" width="14" height="14" rx="3" fill="#fff"/><circle cx="8" cy="8" r="4" fill="none" stroke="#000"/><path d="M4 8h8M8 4v8" stroke="#000"/></svg>
      </li>
    </ul>
  </section>

</main>
</body>
</html>
```